New Advertising Company Business Card

A two sided business card. One side with logo only and the other side with my information and maybe my logo again. Looking for something unique and creative, but not too busy. Info would include my name(Marcus Fenley), President, phone number, address, email address, and website. LOGO IS THE BLUE AND WHITE ONE.

Target Market(s)

CEO/VP Level Audience

Industry/Entity Type

Business

Contact Information for Business Card

In Description.

```html
<!DOCTYPE html>
<html lang="en">
<head>
<meta charset="utf-8">
<title>Halden Advertising – Business Card</title>
<link rel="stylesheet" href="https://fonts.googleapis.com/css2?family=Montserrat:wght@400;600&display=swap">
<style>
  :root {
    --backdrop: #606060;
    --brand-blue: #0b74bf;
    --brand-blue-dark: #0863a6;
    --card-white: #ffffff;
    --card-black: #1e1e1e;
    --ink: #1d1d1f;
  }
  * { box-sizing: border-box; margin: 0; padding: 0; }
  html, body {
    width: 1200px; height: 1200px; overflow: hidden;
    background: var(--backdrop);
    font-family: "Montserrat", Arial, sans-serif;
  }
  .sheet {
    width: 1200px; height: 1200px;
    display: flex; flex-direction: column; align-items: center; justify-content: center;
    gap: 60px;
  }
  .card {
    position: relative; width: 900px; height: 503px;
    border-radius: 14px; overflow: hidden;
  }
  .card-front { background: var(--card-white); }
  .front-band { position: absolute; inset: 0; width: 100%; height: 100%; }
  .holder { position: absolute; left: 64px; top: 218px; color: #fff; }
  .holder-name { font-weight: 600; font-size: 40px; letter-spacing: -0.3px; line-height: 1.1; }
  .holder-title { font-weight: 400; font-size: 27px; margin-top: 2px; }
  .contact-list { list-style: none; margin-top: 34px; }
  .contact-list li {
    display: flex; align-items: center; gap: 9px;
    font-size: 27px; line-height: 35px; font-weight: 400;
  }
  .contact-icon { width: 24px; height: 24px; flex: none; }
  .wordmark {
    position: absolute; text-align: center;
    font-weight: 600; text-transform: uppercase; line-height: 1;
  }
  .card-front .wordmark { right: 64px; top: 120px; width: 360px; color: var(--ink); }
  .wordmark-main { display: block; font-size: 74px; letter-spacing: 6px; }
  .wordmark-sub { display: block; font-size: 28px; letter-spacing: 12px; margin-top: 14px; }
  .address {
    position: absolute; right: 64px; top: 362px;
    text-align: right; color: var(--ink);
    font-size: 27px; line-height: 35px; font-weight: 400;
  }
  .card-back { background: var(--card-black); }
  .card-back .wordmark {
    left: 0; right: 0; top: 50%; transform: translateY(-50%);
    color: #fff;
  }
  .card-back .wordmark-main { font-size: 96px; letter-spacing: 8px; }
  .card-back .wordmark-sub { font-size: 36px; letter-spacing: 16px; margin-top: 18px; }
</style>
</head>
<body>
<main class="sheet">
  <section class="card card-front" aria-label="Card front with contact details">
    <svg class="front-band" viewBox="0 0 900 503" preserveAspectRatio="none" aria-hidden="true">
      <polygon points="0,0 277,0 520,503 0,503" fill="var(--brand-blue)"/>
      <polygon points="250,0 277,0 520,503 493,503" fill="var(--brand-blue-dark)" opacity="0.45"/>
    </svg>
    <div class="holder">
      <h1 class="holder-name">Marcus Fenley</h1>
      <p class="holder-title">President</p>
      <ul class="contact-list">
        <li>
          <svg class="contact-icon" viewBox="0 0 24 24" aria-hidden="true"><circle cx="12" cy="12" r="10.5" fill="none" stroke="#fff" stroke-width="1.6"/><rect x="9" y="6.5" width="6" height="11" rx="1.2" fill="none" stroke="#fff" stroke-width="1.5"/></svg>
          (000) 000-0000
        </li>
        <li>
          <svg class="contact-icon" viewBox="0 0 24 24" aria-hidden="true"><circle cx="12" cy="12" r="10.5" fill="none" stroke="#fff" stroke-width="1.6"/><path d="M8.5 7c-.8.6-1 1.6-.6 2.7 1 2.6 3 4.7 5.6 5.8 1.1.4 2.1.2 2.7-.6l.4-.7-2.2-1.4-1 .9c-1.4-.7-2.4-1.7-3.1-3.1l.9-1L10 7.4z" fill="#fff"/></svg>
          (000) 000-0000
        </li>
        <li>
          <svg class="contact-icon" viewBox="0 0 24 24" aria-hidden="true"><circle cx="12" cy="12" r="10.5" fill="none" stroke="#fff" stroke-width="1.6"/><rect x="7" y="8.5" width="10" height="7" rx="1" fill="#fff"/><path d="M7.5 9l4.5 3.4L16.5 9" fill="none" stroke="var(--brand-blue)" stroke-width="1.1"/></svg>
          name@email.com
        </li>
        <li>
          <svg class="contact-icon" viewBox="0 0 24 24" aria-hidden="true"><circle cx="12" cy="12" r="10.5" fill="none" stroke="#fff" stroke-width="1.6"/><circle cx="12" cy="12" r="5.5" fill="none" stroke="#fff" stroke-width="1.3"/><path d="M6.5 12h11M12 6.5c-2.2 3-2.2 8 0 11M12 6.5c2.2 3 2.2 8 0 11" fill="none" stroke="#fff" stroke-width="1.1"/></svg>
          www.domain.com
        </li>
      </ul>
    </div>
    <div class="wordmark">
      <span class="wordmark-main">Halden</span>
      <span class="wordmark-sub">Advertising</span>
    </div>
    <address class="address" style="font-style: normal;">
      Unit Street<br>Building<br>City, State Zip Code
    </address>
  </section>

  <section class="card card-back" aria-label="Card back with company name">
    <div class="wordmark">
      <span class="wordmark-main">Halden</span>
      <span class="wordmark-sub">Advertising</span>
    </div>
  </section>
</main>
</body>
</html>
```